Training Program Flyers

***Please note an update - the flyers should have somewhere a space that can include a special offer, which can be removed if not applicable with no impact to the design. Have uploaded a graphic of a current example of an offer**

We require 2 flyers to be re-designed which will include:
- Program Flyer
- Training calendar

Current flyers are attached - which are generally 2 pages long.

Program flyers
The newly designed flyer templates should cater for future use across multiple courses and have space for pictures that will be relevant to the content and also allow for additional content to be added if required (ie the template could be extended to a 3rd page)

Training Calendar
This flyer should be flexible to add additional courses as they arise and extend onto further pages easily.

Our branding guidelines and corporate colours should also be followed as attached.

We require editable files in photoshop/illustrator and PDF
The flyers should be A4 in size

Thank you for your time
Corinne

Target Market(s)

Students paying for services

Industry/Entity Type

Training

Font styles to use
Other font styles liked:
• As per brand guidelines

Requirements
Must have
• Corporate Brand Look and Feel

```html
<!DOCTYPE html>
<html lang="en">
<head>
<meta charset="utf-8">
<title>Programs Overview Flyer</title>
<link rel="stylesheet" href="https://fonts.googleapis.com/css2?family=Lato:wght@400;700;900&family=Oswald:wght@300&family=Roboto:wght@700;900&display=swap">
<style>
:root{
  --blue:#1a6fb0;
  --blue-dark:#0d4f8c;
  --blue-light:#3fa7e0;
  --red:#e3261b;
  --red-dark:#c11a10;
  --white:#ffffff;
  --ink:#222222;
}
*{margin:0;padding:0;box-sizing:border-box}
html,body{width:902px;height:1200px;overflow:hidden;background:var(--white)}
.flyer{position:relative;width:902px;height:1200px;overflow:hidden;font-family:"Lato",Arial,sans-serif;background:var(--white)}
.header-panel{position:absolute;left:459px;top:0;width:443px;height:200px;background:linear-gradient(180deg,var(--blue-dark),var(--blue))}
.brand{position:absolute;left:150px;top:58px;display:flex;align-items:center;gap:10px}
.brand-dot{width:26px;height:26px;border-radius:50%;background:var(--red)}
.brand-name{font-family:"Lato",sans-serif;font-weight:900;font-size:34px;color:var(--blue);letter-spacing:-0.5px}
.brand-sub{position:absolute;left:238px;top:104px;font-size:10px;color:var(--red);letter-spacing:1px}
.contacts{position:absolute;right:24px;top:42px;list-style:none;text-align:right;color:var(--white);font-size:19px}
.contacts li{display:flex;justify-content:flex-end;align-items:center;gap:14px;height:32px}
.contacts svg{width:18px;height:18px}
.hero{position:absolute;left:0;top:152px}
.title{position:absolute;left:533px;top:232px;width:330px;text-align:center}
.title-main{font-family:"Roboto",sans-serif;font-weight:900;font-size:52px;color:var(--red);letter-spacing:1px;line-height:1}
.title-sub{font-family:"Oswald",sans-serif;font-weight:300;font-size:86px;color:var(--blue);line-height:1;margin-top:4px}
.offer{position:absolute;left:562px;top:364px;width:250px;height:96px;border-radius:50%;background:var(--white);border:4px solid var(--red);box-shadow:0 0 0 3px var(--blue-light)}
.offer-text{position:absolute;left:22px;top:12px;width:130px;text-align:center;line-height:1.1}
.offer-save{font-family:"Roboto",sans-serif;font-weight:900;font-size:17px;color:var(--red)}
.offer-label{font-weight:700;font-size:12px;color:var(--blue)}
.offer-small{font-size:8px;color:var(--ink)}
.offer-date{font-weight:700;font-size:15px;color:var(--ink)}
.offer-art{position:absolute;right:26px;top:20px;width:56px;height:46px;border-radius:50%;background:linear-gradient(135deg,#5fb2e6,#2a7fc0)}
.programs-col{position:absolute;left:0;top:480px;width:459px;height:720px;background:linear-gradient(90deg,#0f5a9a,#2f8fd0)}
.tab{position:absolute;left:0;width:301px;height:49px;background:linear-gradient(180deg,#f04a2e,var(--red-dark));border-radius:0 26px 26px 0;color:var(--white);font-family:"Roboto",sans-serif;font-weight:700;font-size:16px;line-height:19px;padding:6px 0 0 28px;text-transform:uppercase;box-shadow:2px 2px 4px rgba(0,0,0,.3)}
.blurb{position:absolute;left:28px;width:340px;color:var(--white);font-family:"Roboto",sans-serif;font-weight:700;font-size:13px;line-height:16px}
.blurb small{font-size:11px}
.detail{position:absolute;left:509px;width:393px;background:linear-gradient(90deg,#ffffff 0%,#eeeeee 40%,#c9c9c9 100%);padding:12px 10px 0 0;font-family:"Roboto",sans-serif;font-weight:700;font-size:12.5px;color:var(--ink);line-height:15px}
.detail dl{display:grid;grid-template-columns:55px 1fr;column-gap:2px}
.detail dt{color:var(--red);padding-left:4px}
.detail dd small{font-size:10.5px}
.portrait{position:absolute;left:408px;width:95px;height:95px;border-radius:50%;border:4px solid var(--white);box-shadow:-4px 0 0 3px var(--blue-light);background:linear-gradient(135deg,#e8e8e8,#9a9a9a)}
</style>
</head>
<body>
<main class="flyer">
  <div class="header-panel"></div>

  <div class="brand"><span class="brand-dot"></span><span class="brand-name">northbay skills</span></div>
  <div class="brand-sub">TRAINING COLLEGE</div>

  <ul class="contacts">
    <li>(02) 5550 1840 <svg viewBox="0 0 18 18"><rect x="3" y="1" width="12" height="16" rx="2" fill="#e3261b"/><rect x="5" y="3" width="8" height="6" fill="#fff"/></svg></li>
    <li>www.northbayskills.com <svg viewBox="0 0 18 18"><circle cx="9" cy="9" r="8" fill="#e3261b"/><path d="M1 9h16M9 1c-4 4-4 12 0 16M9 1c4 4 4 12 0 16" stroke="#fff" stroke-width="1.2" fill="none"/></svg></li>
    <li>hello@northbayskills.com <svg viewBox="0 0 18 18"><rect x="1" y="4" width="16" height="11" fill="#e3261b"/><path d="M1 4l8 6 8-6" stroke="#fff" stroke-width="1.3" fill="none"/></svg></li>
  </ul>

  <svg class="hero" width="902" height="330" viewBox="0 0 902 330">
    <defs>
      <linearGradient id="photoFade" x1="0" x2="1" y1="0" y2="0">
        <stop offset="0" stop-color="#6f9fc4"/>
        <stop offset="0.45" stop-color="#9dc1de"/>
        <stop offset="0.8" stop-color="#dbe8f2"/>
        <stop offset="1" stop-color="#ffffff"/>
      </linearGradient>
      <linearGradient id="colBlue" x1="0" x2="1">
        <stop offset="0" stop-color="#0f5a9a"/>
        <stop offset="1" stop-color="#2f8fd0"/>
      </linearGradient>
    </defs>
    <polygon points="0,8 902,82 902,330 0,330" fill="#ffffff"/>
    <g role="img" aria-label="Photo of a smiling student writing at a desk in a classroom">
      <polygon points="0,18 700,66 700,220 0,300" fill="url(#photoFade)"/>
    </g>
    <polygon points="0,-12 459,20 902,58 902,92 459,46 0,12" fill="#e3261b"/>
    <polygon points="0,12 902,92 902,98 0,18" fill="#3fa7e0"/>
    <polygon points="0,296 902,212 902,218 0,302" fill="#3fa7e0"/>
    <polygon points="0,302 902,218 902,238 0,318" fill="#e3261b"/>
    <polygon points="0,318 459,277 459,330 0,330" fill="url(#colBlue)"/>
  </svg>

  <div class="title">
    <div class="title-main">PROGRAMS</div>
    <div class="title-sub">OVERVIEW</div>
  </div>

  <div class="offer">
    <div class="offer-text">
      <div class="offer-save">SAVE $100</div>
      <div class="offer-label">Early Bird Special</div>
      <div class="offer-small">Students who enrol &amp;<br>pay their deposit by</div>
      <div class="offer-date">22nd December</div>
    </div>
    <div class="offer-art" role="img" aria-label="Illustration of a small blue bird"></div>
  </div>

  <section class="programs-col"></section>

  <div class="tab" style="top:467px">Gain foundation skills<br>valued by any employer</div>
  <p class="blurb" style="top:543px">FOUNDATION SKILLS FOR VARIED CAREERS<br>BSB30113 Certificate III in Business</p>

  <div class="tab" style="top:592px">Certificate IV in training<br>and assessment - TAE40110</div>
  <p class="blurb" style="top:656px">Reflect the job roles of individuals delivering training and assessment services in the Vocational Education and Training (VET) sector</p>

  <div class="tab" style="top:728px">Boost your career in<br>aged care</div>
  <p class="blurb" style="top:786px">RAPIDLY GROWING EMPLOYMENT OPPORTUNITIES<br><small>CHC40108 Certificate IV in Aged Care = Career Advancement</small></p>

  <div class="tab" style="top:854px">Join one of the fastest<br>growing sectors</div>
  <p class="blurb" style="top:920px">ENTRY LEVEL STAFF REQUIRED FOR THE<br>AGED CARE INDUSTRY<br><small>CHC30212 Certificate III in Aged Care = Career Pathway</small></p>

  <div class="tab" style="top:990px">Looking for an entry point<br>into the childcare industry</div>
  <p class="blurb" style="top:1050px">KICK START YOUR CAREER DOING<br>SOMETHING YOU LOVE!<br>CHC30113 Certificate III in Early Childhood<br>Education and Care</p>

  <div class="detail" style="top:490px;height:95px"><dl>
    <dt>Dates :</dt><dd>9 February 2015 - 6 May 2015 + work experience on program conclusion (60 hours)</dd>
    <dt>Times :</dt><dd>9.30am – 2.30pm</dd>
    <dt>Venue :</dt><dd>Northbay Skills, 45 Marlow Street Tellbridge NSW 2999</dd></dl></div>
  <div class="portrait" style="top:489px" role="img" aria-label="Portrait photo of a smiling woman"></div>

  <div class="detail" style="top:630px;height:80px"><dl>
    <dt>Dates :</dt><dd>27 Feb 2015 – 29 August 2015</dd>
    <dt>Times :</dt><dd>9.30am to 4.30pm</dd>
    <dt>Venue :</dt><dd>Northbay Skills, 45 Marlow Street Tellbridge NSW</dd></dl></div>
  <div class="portrait" style="top:622px" role="img" aria-label="Photo of a trainer presenting to a small group"></div>

  <div class="detail" style="top:768px;height:80px"><dl>
    <dt>Dates :</dt><dd>17 February 2015 – 19 April 2016</dd>
    <dt>Times :</dt><dd>9.00am – 5.00pm</dd>
    <dt>Venue :</dt><dd>Northbay Skills, 45 Marlow Street, Tellbridge</dd></dl></div>
  <div class="portrait" style="top:760px;background:linear-gradient(135deg,#f1d9c8,#b98a6f)" role="img" aria-label="Close-up photo of an elderly hand held in support"></div>

  <div class="detail" style="top:905px;height:85px"><dl>
    <dt>Dates :</dt><dd>4 Feb 2015 – 8 May 2015</dd>
    <dt>Times :</dt><dd>9am to 2.30pm (except during on the job training)</dd>
    <dt>Venue :</dt><dd>Northbay Skills, 45 Marlow Street TELLBRIDGE NSW<br><small>(except during work placement – venue to be advised)</small></dd></dl></div>
  <div class="portrait" style="top:897px" role="img" aria-label="Portrait photo of a smiling man"></div>

  <div class="detail" style="top:1038px;height:90px"><dl>
    <dt>Dates :</dt><dd>2 February 2015– 23 June 2015</dd>
    <dt>Times :</dt><dd>9.30am – 3.00pm</dd>
    <dt>Venue :</dt><dd>Northbay Skills, 45 Marlow Street Tellbridge NSW 2999</dd></dl></div>
  <div class="portrait" style="top:1034px;background:linear-gradient(135deg,#f4e0c8,#d08a5a)" role="img" aria-label="Photo of a young child playing with paint"></div>
</main>
</body>
</html>
```